Mirela Hartsby ADHD coach needs a flyer

I need a flyer to be sent by email. the copy is attached. It can be changed/reduced to fit the flyer. I would like to keep my website colors. My website is www.mirelahartsby.example - Thank you!

```html
<!DOCTYPE html>
<html lang="en">
<head>
<meta charset="utf-8">
<title>Mirela Hartsby – Academic Success Coaching Flyer</title>
<link rel="stylesheet" href="https://fonts.googleapis.com/css2?family=Montserrat:wght@400;500;600;700;800&display=swap">
<style>
:root{
  --teal:#86adbb;
  --teal-soft:#a9c5cf;
  --panel:#ededed;
  --ink:#2f2f2f;
  --paper:#ffffff;
  --backdrop:#e6e6e6;
  --photo-a:#c9b9b6;
  --photo-b:#6f8f9c;
}
*{box-sizing:border-box;margin:0;padding:0}
html,body{width:1200px;height:880px;overflow:hidden;background:var(--backdrop)}
body{font-family:"Montserrat",sans-serif;color:var(--ink)}
.flyer{position:absolute;left:280px;top:26px;width:640px;height:828px;background:var(--paper);box-shadow:0 6px 22px rgba(0,0,0,.18);overflow:hidden}
.hero-band{position:absolute;left:0;top:0;width:640px;height:360px;background:var(--teal)}
.title{position:absolute;left:240px;top:22px;width:390px;color:#fff;font-weight:800;font-size:25px;line-height:1.1}
.subtitle{position:absolute;left:242px;top:84px;width:380px;color:#fff;font-size:9px;line-height:1.4;font-weight:500}
.portrait{position:absolute;left:0;top:100px;width:230px;height:316px;background:linear-gradient(160deg,var(--photo-b) 0%,var(--photo-a) 55%,#e9dede 100%)}
.intro{position:absolute;left:240px;top:134px;width:400px;background:var(--panel);border-radius:34px 0 0 34px;padding:12px 14px 12px 22px;font-size:7.8px;line-height:1.38}
.intro p+p{margin-top:6px}
.column{position:absolute;display:flex;flex-direction:column;gap:7px;font-size:7.8px;line-height:1.38}
.column-left{left:22px;top:426px;width:296px}
.column-right{left:334px;top:374px;width:306px}
.bar{background:var(--teal);color:#fff;font-weight:700;display:flex;align-items:center;gap:8px;padding:6px 12px}
.chev{font-weight:800;letter-spacing:-2px;font-size:13px;flex:none}
.bar .label{line-height:1.15;font-size:12px}
.tri-list{list-style:none}
.tri-list li{padding-left:13px;position:relative;margin-bottom:3px}
.tri-list li::before{content:"";position:absolute;left:0;top:3px;border-left:6px solid var(--teal);border-top:3.5px solid transparent;border-bottom:3.5px solid transparent}
.dot-list{list-style:none;padding-left:6px}
.dot-list li{padding-left:11px;position:relative}
.dot-list li::before{content:"•";position:absolute;left:0}
.quote-box{border-radius:20px 0 0 20px;padding:9px 14px 6px 16px}
.quote-box h3{text-align:center;font-size:10.5px;font-weight:700;margin-bottom:5px}
.quote{position:relative;padding-left:15px;margin-bottom:5px}
.quote::before{content:"\201C";position:absolute;left:0;top:-3px;font-size:15px;font-weight:800;line-height:1}
.parents{background:var(--panel)}
.students{background:var(--teal-soft)}
.next-steps{text-align:center;padding:0 8px}
.next-steps h3{font-size:10.5px;font-weight:700;margin-bottom:2px}
.next-steps strong{font-weight:700}
</style>
</head>
<body>
<main class="flyer">
  <div class="hero-band"></div>
  <h1 class="title">Helping Your Child with ADHD or Other Learning</h1>
  <p class="subtitle">Academic success coaching that leads to lifelong transformation for students with ADHD and similar challenges that may have impeded their ability to thrive.</p>
  <div class="portrait" role="img" aria-label="Portrait photo of coach Mirela Hartsby in a pale pink blazer, arms crossed"></div>

  <section class="intro">
    <p>Sending your child off to college can feel scary, especially if that college is hundreds of miles away. You worry about how they'll do on their own—whether they'll make friends, earn good grades, and be happy—especially without you there to support them daily. You know your child is bright, and you want them to have a great future, but you're concerned they will struggle without the right support and resources.</p>
    <p>You don't need to feel helpless as you send your child off to this next stage of their lives. Mirela is dedicated to making that transition easier for everyone. Mirela Hartsby has years of experience helping students thrive despite their challenges. She sees your child's potential and helps them see it, too. She provides a safety net as they adjust to a new environment at college. Her services are comprehensive and adaptable, based on the requirements of each individual: helping with course selection and scheduling, time management, study strategies, focus, making new friends, and adapting to change. Through it all, Mirela guides students through fundamental work on mindset to ensure that changes stick.</p>
  </section>

  <div class="column column-left">
    <div class="bar"><span class="chev">›››››</span><span class="label">Empowering Focus:<br>How Mirela Helps</span></div>
    <p>Mirela has taken students from failing to a 3.0 GPA, and from a C student to the Dean's List, in just one semester. It doesn't take years to provide lasting results, all it takes is the right guide.</p>
    <p>Uniquely positioned to help your child, Mirela:</p>
    <ul class="tri-list">
      <li>Tailors support so that your child improves focus and maximizes their potential in college and beyond.</li>
      <li>Understands your child's unique needs - she sees the gifts that others often miss.</li>
      <li>Knows the academic landscape intimately, including the challenges faced by students with ADHD and other conditions.</li>
      <li>Helps with the logistics of scheduling in a way that most advisors can't, enrolling students in the courses that best suit their learning style.</li>
      <li>Nurtures the brilliance in your bright child.</li>
      <li>Provides a balance between encouraging students and challenging them.</li>
    </ul>
    <div class="bar"><span class="chev">›››››</span><span class="label">Realizing Potential: The Transformation<br>You'll See in Your Child</span></div>
    <ul class="dot-list">
      <li>A mindset of self-belief and increased confidence.</li>
      <li>Higher grades and the drive to graduate.</li>
      <li>Social integration and making friends.</li>
      <li>Happiness and fulfilment.</li>
      <li>A deep sense of personal achievement and pride.</li>
    </ul>
  </div>

  <div class="column column-right">
    <div class="bar"><span class="chev">›››››</span><span class="label">You Will Have:</span></div>
    <ul class="dot-list">
      <li>Less stress, knowing that your child is in good hands.</li>
      <li>Fewer sleepless nights worrying about your child.</li>
      <li>Confidence that they are receiving the right support.</li>
      <li>Joy and pride at seeing them do well.</li>
    </ul>
    <section class="quote-box parents">
      <h3>What Parents Say</h3>
      <p class="quote">Mirela was the glue that kept our daughter in college... as our daughter's Academic Coach, [she] gave our daughter the ability to finish strong by empowering her with the skills needed to be successful." - Lorna</p>
      <p class="quote">Mirela has always told my daughter not that she can succeed, but that she will succeed!" —Maren</p>
    </section>
    <section class="quote-box students">
      <h3>What Students Say</h3>
      <p class="quote">Last semester I completed all 18 hours and I had the highest GPA I've ever had!" —Former student</p>
      <p class="quote">Under her instruction, my grades began to improve. I ended up making the Dean's List during my time at Ridgeway, and I was also inducted into Delta Kappa Rho. I am currently in my first year of law school at Halverson University, a top tier school!" —Former student</p>
    </section>
    <section class="next-steps">
      <h3>Next Steps</h3>
      <p>To learn more and discuss your child's individual needs, call <strong>555 010 4821</strong> or email <strong>coach@mirelahartsby.example</strong></p>
    </section>
  </div>
</main>
</body>
</html>
```